Barvo Grand Opening

I need a one sided flyer that advertises my grand opening for our new equipment dealership.

Grand Opening

New and Used Equipment Sales
Equipment Rentals
Residential, Commercial and Industrial Rental Equipment
Construction and Industrial Supply
Custom Metal Fabrication
Mobile Welding Service
Pickup and Delivery Service
24hr. Emergency Dedicated Service

Now Open!

4362 Mellowfen HWY
Brindale, SC 29000

(864) 555 - 0143

7:00am-7:00pm Monday - Friday
8:00am-3:00pm Saturday

www.barvogear.example

```html
<!DOCTYPE html>
<html lang="en">
<head>
<meta charset="utf-8">
<title>Barvo Grand Opening Flyer</title>
<link rel="stylesheet" href="https://fonts.googleapis.com/css2?family=Archivo+Black&family=Oswald:wght@500;600&family=Poppins:wght@500;600;700&display=swap">
<style>
  :root {
    --page-bg: #f3f3f3;
    --flyer-black: #0b0b0c;
    --flyer-dark: #1a1a1c;
    --brand-red: #e91f26;
    --deep-red: #8e0d12;
    --silver-light: #f4f4f4;
    --silver-mid: #a9a9a9;
    --silver-dark: #6d6d6d;
    --white: #ffffff;
    --ink: #1b1b1b;
  }
  html, body {
    margin: 0;
    padding: 0;
    width: 1200px;
    height: 2261px;
    overflow: hidden;
    background: var(--page-bg);
  }
  .flyer {
    position: absolute;
    left: 40px;
    top: 405px;
    width: 1120px;
    height: 1451px;
    box-shadow: 0 30px 60px rgba(0,0,0,0.35);
  }
  .flyer svg { display: block; }
  .brand-name { font-family: "Poppins", sans-serif; font-weight: 700; font-size: 60px; fill: var(--white); }
  .headline { font-family: "Archivo Black", sans-serif; }
  .hours-text { font-family: "Poppins", sans-serif; font-weight: 600; font-size: 35px; fill: var(--white); }
  .address { font-family: "Poppins", sans-serif; font-weight: 500; font-size: 30px; fill: var(--white); }
  .service-label { font-family: "Poppins", sans-serif; font-weight: 500; font-size: 21px; fill: var(--white); }
  .badge-number { font-family: "Oswald", sans-serif; font-weight: 600; font-size: 80px; fill: var(--brand-red); }
  .badge-top { font-family: "Oswald", sans-serif; font-weight: 600; font-size: 38px; fill: var(--white); }
  .badge-bottom { font-family: "Oswald", sans-serif; font-weight: 500; font-size: 31px; fill: var(--ink); }
  .sign-text { font-family: "Poppins", sans-serif; font-weight: 700; font-size: 52px; letter-spacing: 5px; fill: var(--white); }
  .contact-text { font-family: "Poppins", sans-serif; font-weight: 500; font-size: 34px; fill: var(--white); }
  .icon-line { fill: none; stroke: var(--white); stroke-width: 3; stroke-linejoin: round; stroke-linecap: round; }
</style>
</head>
<body>
<div class="flyer">
<svg width="1120" height="1451" viewBox="0 0 1120 1451" xmlns="http://www.w3.org/2000/svg">
  <defs>
    <radialGradient id="bgGlow" cx="50%" cy="35%" r="75%">
      <stop offset="0" stop-color="#242427"/>
      <stop offset="1" stop-color="#080809"/>
    </radialGradient>
    <linearGradient id="redText" x1="0" y1="0" x2="0" y2="1">
      <stop offset="0" stop-color="#ff2a2f"/>
      <stop offset="0.55" stop-color="#d8141b"/>
      <stop offset="1" stop-color="#6e080c"/>
    </linearGradient>
    <linearGradient id="silverText" x1="0" y1="0" x2="0" y2="1">
      <stop offset="0" stop-color="#ffffff"/>
      <stop offset="0.45" stop-color="#d9d9d9"/>
      <stop offset="0.6" stop-color="#8a8a8a"/>
      <stop offset="1" stop-color="#f0f0f0"/>
    </linearGradient>
    <linearGradient id="silverBar" x1="0" y1="0" x2="1" y2="0">
      <stop offset="0" stop-color="#9a9a9a"/>
      <stop offset="0.5" stop-color="#f2f2f2"/>
      <stop offset="1" stop-color="#8c8c8c"/>
    </linearGradient>
    <linearGradient id="redBand" x1="0" y1="0" x2="0" y2="1">
      <stop offset="0" stop-color="#f2262d"/>
      <stop offset="1" stop-color="#c9121a"/>
    </linearGradient>
    <linearGradient id="ringSilver" x1="0" y1="0" x2="1" y2="1">
      <stop offset="0" stop-color="#ffffff"/>
      <stop offset="0.5" stop-color="#8d8d8d"/>
      <stop offset="1" stop-color="#e8e8e8"/>
    </linearGradient>
  </defs>

  <!-- background -->
  <rect class="flyer-bg" width="1120" height="1451" fill="url(#bgGlow)"/>
  <polygon points="0,860 260,1000 0,1130" fill="#121214"/>
  <polygon points="1120,860 860,1000 1120,1130" fill="#121214"/>

  <!-- brand -->
  <text class="brand-name" x="560" y="106" text-anchor="middle">Barvo</text>

  <!-- headline -->
  <text class="headline" x="237" y="306" font-size="175" textLength="646" lengthAdjust="spacingAndGlyphs" fill="url(#redText)">GRAND</text>
  <text class="headline" x="149" y="449" font-size="175" textLength="822" lengthAdjust="spacingAndGlyphs" fill="url(#silverText)">OPENING</text>

  <!-- red chevron band -->
  <polygon class="chevron-band" points="0,562 560,781 1120,562 1120,635 560,851 0,635" fill="url(#redBand)"/>
  <polyline points="0,641 560,858 1120,641" fill="none" stroke="url(#silverBar)" stroke-width="5"/>
  <polygon points="0,650 560,866 1120,650 1120,700 560,920 0,700" fill="#0d0d0e" opacity="0.6"/>

  <!-- hours table -->
  <g class="hours-table">
    <rect x="184" y="486" width="370" height="119" fill="#0a0a0a" stroke="var(--white)" stroke-width="3"/>
    <rect x="554" y="486" width="400" height="119" fill="var(--brand-red)" stroke="var(--white)" stroke-width="3"/>
    <line x1="184" y1="545" x2="954" y2="545" stroke="#5a5a5a" stroke-width="1.5"/>
    <text class="hours-text" x="216" y="530">7:00AM-7:00PM</text>
    <text class="hours-text" x="216" y="584">8:00AM-3:00PM</text>
    <text class="hours-text" x="584" y="530">MONDAY - FRIDAY</text>
    <text class="hours-text" x="584" y="584">SATURDAY</text>
  </g>

  <!-- address -->
  <text class="address" x="560" y="657" text-anchor="middle">4362 Mellowfen HWY</text>
  <text class="address" x="560" y="695" text-anchor="middle">Brindale, SC 29000</text>

  <!-- services -->
  <g class="service-dividers" stroke="#3a3a3c" stroke-width="2">
    <line x1="223" y1="872" x2="223" y2="1083"/>
    <line x1="387" y1="872" x2="387" y2="1083"/>
    <line x1="571" y1="872" x2="571" y2="1083"/>
    <line x1="747" y1="872" x2="747" y2="1083"/>
    <line x1="917" y1="872" x2="917" y2="1083"/>
  </g>
  <g class="service-rings" fill="#0c0c0c" stroke="url(#ringSilver)" stroke-width="6">
    <circle cx="139" cy="924" r="52"/>
    <circle cx="304" cy="924" r="52"/>
    <circle cx="479" cy="924" r="52"/>
    <circle cx="663" cy="924" r="52"/>
    <circle cx="834" cy="924" r="52"/>
    <circle cx="994" cy="924" r="52"/>
  </g>
  <!-- sale tag -->
  <g class="icon-line" transform="translate(139 924) rotate(-40)">
    <path d="M-26,-14 H16 L28,0 L16,14 H-26 Z"/>
    <circle cx="14" cy="0" r="3"/>
    <text x="-6" y="5" font-family="Poppins, sans-serif" font-size="13" font-weight="600" fill="#fff" stroke="none" text-anchor="middle">SALE</text>
  </g>
  <!-- rent sign -->
  <g class="icon-line">
    <path d="M296,906 L304,896 L312,906"/>
    <rect x="280" y="906" width="48" height="28" rx="3"/>
    <text x="304" y="926" font-family="Poppins, sans-serif" font-size="13" font-weight="600" fill="#fff" stroke="none" text-anchor="middle">RENT</text>
  </g>
  <!-- buildings -->
  <g class="icon-line">
    <rect x="482" y="898" width="18" height="46"/>
    <path d="M458,944 V922 L472,910 L486,922"/>
    <line x1="450" y1="944" x2="508" y2="944"/>
    <rect x="466" y="930" width="10" height="14"/>
  </g>
  <!-- crane -->
  <g class="icon-line">
    <line x1="652" y1="896" x2="652" y2="948"/>
    <line x1="640" y1="902" x2="690" y2="902"/>
    <line x1="682" y1="902" x2="682" y2="920"/>
    <rect x="674" y="920" width="16" height="12"/>
    <line x1="642" y1="948" x2="662" y2="948"/>
  </g>
  <!-- fabrication grid -->
  <g class="icon-line">
    <rect x="812" y="902" width="44" height="44" rx="4"/>
    <line x1="827" y1="902" x2="827" y2="946"/>
    <line x1="841" y1="902" x2="841" y2="946"/>
    <line x1="812" y1="917" x2="856" y2="917"/>
    <line x1="812" y1="931" x2="856" y2="931"/>
  </g>
  <!-- welding arm -->
  <g class="icon-line">
    <rect x="970" y="936" width="26" height="10"/>
    <path d="M983,936 L978,914 L1000,902 L1012,916"/>
    <circle cx="978" cy="914" r="4"/>
    <circle cx="1000" cy="902" r="4"/>
    <rect x="1004" y="930" width="16" height="16"/>
  </g>

  <g class="service-labels" text-anchor="middle">
    <text class="service-label" x="139" y="1016">New and Used<tspan x="139" dy="24">Equipment</tspan><tspan x="139" dy="24">Sales</tspan></text>
    <text class="service-label" x="304" y="1016">Equipment<tspan x="304" dy="24">Rentals</tspan></text>
    <text class="service-label" x="479" y="1016">Residential,<tspan x="479" dy="24">Commercial &amp;</tspan><tspan x="479" dy="24">Industrial Rental</tspan><tspan x="479" dy="24">Equipment</tspan></text>
    <text class="service-label" x="663" y="1016">Construction<tspan x="663" dy="24">and Industrial</tspan><tspan x="663" dy="24">Supply</tspan></text>
    <text class="service-label" x="834" y="1016">Custom Metal<tspan x="834" dy="24">Fabrication</tspan></text>
    <text class="service-label" x="994" y="1016">Mobile<tspan x="994" dy="24">Welding</tspan><tspan x="994" dy="24">Service</tspan></text>
  </g>

  <!-- 24hr emergency badge -->
  <g class="emergency-badge">
    <path d="M108,1146 A40,40 0 1 0 140,1168" fill="none" stroke="url(#ringSilver)" stroke-width="7" stroke-linecap="round"/>
    <path d="M100,1138 L112,1146 L100,1154" fill="none" stroke="#cfcfcf" stroke-width="5"/>
    <path d="M96,1160 V1186 H82" fill="none" stroke="#ffffff" stroke-width="5" stroke-linecap="round"/>
    <text class="badge-number" x="128" y="1222" textLength="134" lengthAdjust="spacingAndGlyphs">24HR</text>
    <polygon points="270,1141 520,1141 540,1186 270,1186" fill="var(--brand-red)"/>
    <rect x="270" y="1188" width="306" height="46" rx="3" fill="url(#silverBar)"/>
    <text class="badge-top" x="280" y="1180">EMERGENCY</text>
    <text class="badge-bottom" x="280" y="1225" textLength="286" lengthAdjust="spacingAndGlyphs">DEDICATED SERVICE</text>
  </g>

  <!-- pickup and delivery badge -->
  <g class="delivery-badge">
    <rect x="672" y="1152" width="92" height="74" rx="4" fill="url(#silverBar)"/>
    <path d="M668,1226 V1184 L646,1172 H620 L610,1196 V1226 Z" fill="#f2f2f2"/>
    <path d="M624,1180 H644 L652,1196 H618 Z" fill="#1a1a1a"/>
    <circle cx="634" cy="1230" r="13" fill="#f2f2f2" stroke="#111" stroke-width="5"/>
    <circle cx="735" cy="1230" r="13" fill="#f2f2f2" stroke="#111" stroke-width="5"/>
    <polygon points="772,1141 1020,1141 1040,1186 772,1186" fill="var(--brand-red)"/>
    <rect x="772" y="1188" width="288" height="46" rx="3" fill="url(#silverBar)"/>
    <text class="badge-top" x="782" y="1180">PICKUP AND</text>
    <text class="badge-bottom" x="782" y="1225" textLength="268" lengthAdjust="spacingAndGlyphs">DELIVERY SERVICE</text>
  </g>

  <!-- now open sign -->
  <g class="now-open-sign">
    <polyline points="95,1318 281,1267 467,1318" fill="none" stroke="#d0d0d0" stroke-width="2"/>
    <circle cx="281" cy="1267" r="6" fill="#ffffff"/>
    <rect x="74" y="1318" width="411" height="71" rx="14" fill="var(--brand-red)"/>
    <rect x="80" y="1324" width="399" height="59" rx="10" fill="none" stroke="#ffffff" stroke-width="3"/>
    <text class="sign-text" x="280" y="1373" text-anchor="middle">NOW OPEN</text>
  </g>

  <!-- contact -->
  <g class="contact">
    <circle cx="555" cy="1324" r="15" fill="var(--brand-red)"/>
    <path d="M549,1315 c-3,3 -2,9 3,14 s11,6 14,3 l-4,-4 -3,2 c-3,-1 -6,-4 -7,-7 l2,-3 z" fill="#ffffff"/>
    <text class="contact-text" x="585" y="1336">(864) 555 - 0143</text>
    <circle cx="555" cy="1372" r="15" fill="none" stroke="var(--brand-red)" stroke-width="4"/>
    <ellipse cx="555" cy="1372" rx="6" ry="15" fill="none" stroke="var(--brand-red)" stroke-width="3"/>
    <line x1="540" y1="1372" x2="570" y2="1372" stroke="var(--brand-red)" stroke-width="3"/>
    <text class="contact-text" x="591" y="1384">www.barvogear.example</text>
  </g>
</svg>
</div>
</body>
</html>
```